R&t Subterra

We specialize in CIPP pipe lining but do other underground utilities trenchless as well.

Target Market(s)

Trenchless sewer replacement

Contact Information for Business Card

Gavin Holtby 715-482-6130 Birchwood falls, mn

```html
<!DOCTYPE html>
<html lang="en">
<head>
<meta charset="UTF-8">
<title>R&amp;t Subterra – Business Card</title>
<link href="https://fonts.googleapis.com/css2?family=Krona+One&family=Poppins:wght@500;600;700&display=swap" rel="stylesheet">
<style>
  :root {
    --page-bg: #e9eaec;
    --card-blue-a: #2f86cb;
    --card-blue-b: #3da2d6;
    --brand-blue: #2a7fc6;
    --brand-blue-deep: #1f6fb4;
    --name-blue-light: #4aa8e0;
    --text-grey: #8a8a8c;
    --rule-grey: #9a9a9a;
    --wave-grey: #a8a8a8;
    --white: #ffffff;
  }
  * { margin: 0; padding: 0; box-sizing: border-box; }
  html, body {
    width: 900px; height: 1200px; overflow: hidden;
    background: var(--page-bg);
    font-family: "Poppins", sans-serif;
  }
  .canvas { position: relative; width: 900px; height: 1200px; }

  .card {
    position: absolute; left: 135px; width: 631px; height: 358px;
    border-radius: 12px; overflow: hidden;
  }
  .card--front {
    top: 215px;
    background: linear-gradient(120deg, var(--card-blue-a), var(--card-blue-b));
    display: flex; align-items: center; justify-content: center;
  }
  .card--back { top: 628px; background: var(--white); }

  .brand {
    display: flex; align-items: center; gap: 14px;
    font-family: "Poppins", sans-serif; font-weight: 700;
  }
  .brand__dot { border-radius: 50%; flex: none; }
  .card--front .brand { font-size: 46px; color: var(--brand-blue-deep); }
  .card--front .brand__dot { width: 60px; height: 60px; background: var(--brand-blue-deep); }

  .card--back .brand {
    position: absolute; left: 50px; top: 152px;
    font-size: 29px; color: var(--brand-blue);
  }
  .card--back .brand__dot { width: 46px; height: 46px; background: var(--brand-blue); }

  .divider {
    position: absolute; left: 315px; top: 113px;
    width: 1px; height: 133px; background: var(--rule-grey);
  }

  .contact { position: absolute; left: 339px; top: 104px; }
  .contact__name {
    font-family: "Krona One", sans-serif; font-weight: 400;
    font-size: 29px; line-height: 31px; text-transform: uppercase;
    letter-spacing: 0.5px;
    -webkit-text-stroke: 0.8px currentColor;
  }
  .contact__name span { display: block; }
  .contact__first { color: var(--brand-blue); }
  .contact__last { color: var(--name-blue-light); }

  .contact__row {
    display: flex; align-items: center; gap: 8px;
    color: var(--text-grey); font-weight: 600;
  }
  .contact__row svg { flex: none; }
  .contact__phone { margin-top: 19px; font-size: 19px; letter-spacing: 4px; font-weight: 700; }
  .contact__place { margin-top: 8px; font-size: 17px; }

  .wave { position: absolute; left: 0; bottom: 0; width: 631px; height: 90px; }
</style>
</head>
<body>
<div class="canvas">

  <section class="card card--front" aria-label="Card front">
    <div class="brand">
      <span class="brand__dot"></span>
      <span class="brand__name">R&amp;t Subterra</span>
    </div>
  </section>

  <section class="card card--back" aria-label="Card back">
    <div class="brand">
      <span class="brand__dot"></span>
      <span class="brand__name">R&amp;t Subterra</span>
    </div>

    <div class="divider"></div>

    <div class="contact">
      <h1 class="contact__name">
        <span class="contact__first">Gavin</span>
        <span class="contact__last">Holtby</span>
      </h1>
      <p class="contact__row contact__phone">
        <svg width="17" height="17" viewBox="0 0 24 24" aria-hidden="true">
          <path fill="#2a7fc6" d="M6.6 10.8c1.4 2.8 3.8 5.1 6.6 6.6l2.2-2.2c.3-.3.7-.4 1-.2 1.1.4 2.3.6 3.6.6.6 0 1 .4 1 1V20c0 .6-.4 1-1 1C10.6 21 3 13.4 3 4c0-.6.4-1 1-1h3.5c.6 0 1 .4 1 1 0 1.3.2 2.5.6 3.6.1.3 0 .7-.2 1L6.6 10.8z"/>
        </svg>
        715-482-6130
      </p>
      <p class="contact__row contact__place">
        <svg width="17" height="21" viewBox="0 0 24 30" aria-hidden="true">
          <path fill="#4aa8e0" d="M12 0C5.9 0 1 4.9 1 11c0 8 11 19 11 19s11-11 11-19C23 4.9 18.1 0 12 0zm0 15a4 4 0 1 1 0-8 4 4 0 0 1 0 8z"/>
        </svg>
        Birchwood falls, mn
      </p>
    </div>

    <svg class="wave" viewBox="0 0 631 90" preserveAspectRatio="none" aria-hidden="true">
      <defs>
        <linearGradient id="waveBlue" x1="0" y1="0" x2="1" y2="0">
          <stop offset="0" stop-color="#2b80c8"/>
          <stop offset="0.65" stop-color="#4aaae0"/>
          <stop offset="1" stop-color="#3a90d2"/>
        </linearGradient>
      </defs>
      <path fill="var(--wave-grey)" d="M0 4 C70 30 150 52 230 52 C330 52 420 4 530 2 C580 1 615 14 631 24 L631 28 C600 18 570 8 530 8 C430 10 330 56 230 56 C150 56 70 34 0 10 Z"/>
      <path fill="url(#waveBlue)" d="M0 20 C70 44 150 56 230 56 C330 56 430 10 530 8 C570 8 600 18 631 30 L631 90 L0 90 Z"/>
    </svg>
  </section>

</div>
</body>
</html>
```